Automotive component supplier needs a business card design

We need a business card design for our company called Velmar Global Components Ltd based in the UK. We are a supplier of interior and exterior components to premium car manufacturers such as Corvane Hale, Durrant Fyfe, Maxtorn and Valdessimo. We would like to see a modern business card design that uses the colour blue.

Target Market(s)

Premium automotive car manufacturers.

Industry/Entity Type

Automotive

Contact Information for Business Card

Company Name : Velmar Global Components Limited
Address: 17 Tamsey Yard, Upper Drisk, Warwick, CV31 8RJ, United Kingdom
Web Address : www.velmarparts-example.co.uk

Font styles to use
Other font styles liked:
• Helvetica

Colors
3176b5
0255a3
85acd3
cfdeed
cee9f5
85cae6
34a6d7
0692cd
9bcb3c

Requirements
Must have
• Clear company logo and a mixture of blue colours.
Nice to have
• A high quality modern image.
Should not have
• Multiple colours.

```html
<!DOCTYPE html>
<html lang="en">
<head>
<meta charset="utf-8">
<title>Velmar Global Components – Business Card</title>
<link rel="stylesheet" href="https://fonts.googleapis.com/css2?family=Lato:wght@400;700&family=Barlow+Semi+Condensed:wght@600&display=swap">
<style>
  :root {
    --page-bg: #e9edf1;
    --card-white: #f7f7f7;
    --map-light: #eaeaea;
    --brand-blue: #0692cd;
    --deep-blue: #0255a3;
    --mid-blue: #3176b5;
    --accent-green: #9bcb3c;
    --text-dark: #3a3a3a;
    --white: #ffffff;
  }
  * { box-sizing: border-box; margin: 0; padding: 0; }
  html, body { width: 1200px; height: 934px; overflow: hidden; }
  body {
    background: var(--page-bg);
    font-family: "Lato", Helvetica, Arial, sans-serif;
    position: relative;
  }
  .card {
    position: absolute;
    left: 293px;
    width: 610px;
    height: 348px;
    border-radius: 18px;
    overflow: hidden;
    box-shadow: 0 6px 14px rgba(0,0,0,.25);
  }
  .card--front { top: 90px; background: var(--card-white); }
  .card--back {
    top: 492px;
    background: radial-gradient(ellipse at 45% 25%, #1a8fd0 0%, #0a78b8 45%, #06609e 100%);
  }
  .map-area { position: absolute; }
  .card--front .map-area {
    left: 20px; top: 30px; width: 570px; height: 290px;
    background: radial-gradient(ellipse at 60% 40%, #ececec 0%, var(--card-white) 75%);
  }
  .card--back .map-area {
    left: 40px; top: 0; width: 540px; height: 290px;
    background: radial-gradient(ellipse at 55% 30%, rgba(255,255,255,.08) 0%, rgba(255,255,255,0) 70%);
  }
  .wordmark { position: absolute; font-family: "Barlow Semi Condensed", Helvetica, sans-serif; font-weight: 600; }
  .wordmark__name { display: flex; align-items: center; gap: 10px; letter-spacing: 1px; line-height: 1; }
  .wordmark__mark { width: 12px; height: 12px; background: var(--accent-green); }
  .card--front .wordmark { left: 47px; top: 44px; color: var(--brand-blue); }
  .card--front .wordmark__name { font-size: 50px; }
  .card--front .wordmark__sub { font-size: 17px; letter-spacing: 2.4px; margin-top: 4px; }
  .card--back .wordmark { left: 0; right: 0; top: 130px; color: var(--white); text-align: center; }
  .card--back .wordmark__name { font-size: 64px; justify-content: center; }
  .card--back .wordmark__sub { font-size: 21px; letter-spacing: 3px; margin-top: 8px; }
  .holder { position: absolute; right: 48px; top: 150px; text-align: right; }
  .holder__name {
    font-family: "Barlow Semi Condensed", Helvetica, sans-serif;
    font-weight: 600; font-size: 26px; color: var(--brand-blue); line-height: 1;
  }
  .holder__title { font-size: 18px; color: var(--text-dark); line-height: 1.1; margin-top: 2px; }
  .divider { position: absolute; left: 47px; right: 48px; top: 198px; height: 1px; background: var(--brand-blue); }
  .divider::after {
    content: ""; position: absolute; right: -2px; top: -2px;
    width: 5px; height: 5px; border-radius: 50%; background: var(--accent-green);
  }
  .address { position: absolute; left: 47px; top: 214px; font-size: 15.5px; color: var(--text-dark); line-height: 18.5px; }
  .address__company { color: var(--brand-blue); font-weight: 700; font-size: 16px; margin-bottom: 3px; }
  .contact { position: absolute; right: 48px; top: 216px; list-style: none; font-size: 15.5px; color: var(--text-dark); line-height: 19px; text-align: right; }
  .contact li { display: flex; justify-content: flex-end; align-items: center; gap: 8px; }
  .contact .is-primary { font-weight: 700; }
  .contact svg { width: 12px; height: 12px; fill: var(--brand-blue); }
  .wave { position: absolute; left: 0; bottom: 0; width: 610px; height: 348px; }
  .web {
    position: absolute; left: 94px; right: 108px; top: 280px;
    display: flex; align-items: center; gap: 8px; color: var(--white); font-size: 19px;
  }
  .web__rule { flex: 1; height: 1px; background: var(--white); }
  .web svg { width: 14px; height: 14px; }
</style>
</head>
<body>

<section class="card card--front">
  <div class="map-area" role="img" aria-label="Faint world map background"></div>
  <svg class="wave" viewBox="0 0 610 348" aria-hidden="true">
    <defs>
      <linearGradient id="band-blue" x1="0" x2="1">
        <stop offset="0" stop-color="#0255a3"/>
        <stop offset="0.7" stop-color="#0692cd"/>
        <stop offset="1" stop-color="#0a7fbf"/>
      </linearGradient>
    </defs>
    <path d="M0,285 C110,320 250,334 390,312 C490,296 560,292 610,300 L610,348 L0,348 Z" fill="#9bcb3c"/>
    <path d="M0,310 C120,338 260,334 400,318 C500,306 570,303 610,307 L610,348 L0,348 Z" fill="url(#band-blue)"/>
  </svg>

  <div class="wordmark">
    <div class="wordmark__name">VELMAR <span class="wordmark__mark"></span></div>
    <div class="wordmark__sub">GLOBAL COMPONENTS</div>
  </div>

  <div class="holder">
    <div class="holder__name">ROWAN PETRIE</div>
    <div class="holder__title">General Manager</div>
  </div>

  <div class="divider"></div>

  <address class="address" style="font-style:normal">
    <div class="address__company">Velmar Global Components Limited</div>
    17 Tamsey Yard, Upper Drisk<br>
    Warwick, CV31 8RJ<br>
    United Kingdom
  </address>

  <ul class="contact">
    <li class="is-primary">+44 1632 960418
      <svg viewBox="0 0 24 24"><path d="M6.6 10.8a15 15 0 0 0 6.6 6.6l2.2-2.2c.3-.3.7-.4 1-.2 1.1.4 2.3.6 3.6.6.6 0 1 .4 1 1V20c0 .6-.4 1-1 1A17 17 0 0 1 3 4c0-.6.4-1 1-1h3.5c.6 0 1 .4 1 1 0 1.3.2 2.5.6 3.6.1.3 0 .7-.2 1z"/></svg>
    </li>
    <li>+44 7700 900512
      <svg viewBox="0 0 24 24"><path d="M7 1h10a2 2 0 0 1 2 2v18a2 2 0 0 1-2 2H7a2 2 0 0 1-2-2V3a2 2 0 0 1 2-2zm0 3v14h10V4z"/></svg>
    </li>
    <li>rowan@velmarparts-example.co.uk
      <svg viewBox="0 0 24 24"><path d="M2 5h20v14H2zm2 2v.5l8 5 8-5V7l-8 5z"/></svg>
    </li>
  </ul>
</section>

<section class="card card--back">
  <div class="map-area" role="img" aria-label="Subtle world map in deeper blue tones"></div>
  <div class="wordmark">
    <div class="wordmark__name">VELMAR <span class="wordmark__mark"></span></div>
    <div class="wordmark__sub">GLOBAL COMPONENTS</div>
  </div>
  <div class="web">
    <span class="web__rule"></span>
    <svg viewBox="0 0 24 24" aria-hidden="true"><circle cx="12" cy="12" r="10" fill="#ffffff"/><path d="M12 2v20M2 12h20" stroke="#0a78b8" stroke-width="1.6"/></svg>
    <span>velmarparts-example.co.uk</span>
    <span class="web__rule"></span>
  </div>
</section>

</body>
</html>
```